More Modern Look Required! Industry leading Property Management company needs a new website!

We are wanting to make our website more modern, as we find it is too cluttered, seems "old" and we want a new look. (www.brightholtrm.com)

We are wanting something fresh, clean and responsive, something that aligns with today's social media demands, something that allows our potential customers to immediately get a sense of the type of company we are.

Our current website was created on Wordpress and we will be keeping that core platform but wanting a new look and feel to it. The only thing we want to keep on the website is our "FOR RENT" page, although again we are open to having that look completely different as well (our programmers can adapt the functionality later)

Here is a synopsis of our branding statements:

CORE VALUES:
1. Passion
2. Innovation
3. Integrity (doing the right thing, even when it's difficult)
4. Empathy
5. Education

CORE FOCUS:
Our vision is to be the premier company for the delivery of all aspects of property management showing our passion for this industry, by innovating our service using cutting-edge technology, helping and educating investors to create aspirational and sustainable communities, adding value to their real estate assets, and working in partnership with all stakeholders including residents, showing empathy and integrity.

Brand Essence

When our customers experience our product or service, it brings forth an emotion of absolute trust that we have their best interests at heart

Brand Personality

We are a company that is passionate about our customers, our company and our vision to be leaders in the field of property management. We are visionaries that aren't afraid to use cutting edge technologies to improve our products and service.

Position or Value Proposition

To whom are we speaking?
- real estate investors, including first timers that are giving us their first starter home. They are not "big time" investors, and because they are giving us their first home (in contrast to an investor buying a rental property, often sight unseen) they are more emotionally tied to their property and will require a company that inspires trust and confidence.

What is our brand promise?
- we will do our best to serve our clients, both owners and tenants, to give them prompt communication, clear, concise answers to their questions, and look after their property quickly and competently.

Why is our product different than the competition and why should our customers care?
- Our management product is superior because we use a combination of technology and strict procedures to ensure each client's experience is consistent, each and every time.

Industry/Entity Type

Real Estate and Property Management

Number of Pages Required

5+ page

Requirements
Must have
• Must be compatible on Wordpress, our existing web platform. Please see our existing website at www.brightholtrm.com to familiarize yourself with our current site. Must incorporate For Rent section
Nice to have
• Built in reviews, contact us form, awards page including Resident Laurel Prizes (we just won again for Best Property Management Company, 8 years in a row)
Should not have
• Too many pages. Currently we feel there is too much information on each tab, and we can consolidate into about 5 or 6 tabs.

```html
<!DOCTYPE html>
<html lang="en">
<head>
<meta charset="utf-8">
<title>Brightholt Residential Management</title>
<link href="https://fonts.googleapis.com/css2?family=Lora:ital,wght@0,400;0,500;0,600;1,400&family=Inter:wght@400;500;600&display=swap" rel="stylesheet">
<style>
:root{
  --blue:#1a8ad4;
  --blue-dark:#146fb0;
  --ink:#2b2f36;
  --muted:#7a8089;
  --line:#e3e6ea;
  --grey-bg:#f5f6f8;
  --ice-bg:#eef5f9;
  --footer:#2a2a2c;
  --red:#e84a5f;
  --star:#f3b319;
  --white:#ffffff;
}
*{box-sizing:border-box;margin:0;padding:0}
html,body{width:1200px;height:1200px;overflow:hidden;background:var(--white)}
body{position:relative;font-family:'Inter',sans-serif;color:var(--ink)}
.page{position:absolute;left:486px;top:0;width:1440px;height:7547px;transform:scale(0.159);transform-origin:0 0;overflow:hidden;background:var(--white)}
.abs{position:absolute}
.serif{font-family:'Lora',serif}
.btn{position:absolute;display:flex;align-items:center;justify-content:center;font-size:15px;font-weight:500;border-radius:6px;white-space:nowrap}
.btn-blue{background:var(--blue);color:var(--white)}
.btn-ghost{background:var(--white);border:1px solid var(--line);color:var(--ink)}
/* header */
.topbar{top:0;left:0;width:1440px;height:109px;background:var(--white)}
.brand{display:flex;align-items:center;gap:14px;font-family:'Lora',serif;font-weight:600;font-size:26px;color:var(--blue);white-space:nowrap}
.brand-mark{width:34px;height:34px;background:var(--blue);border-radius:4px}
.contact-line{font-size:13px;line-height:22px;color:var(--ink);white-space:nowrap}
.contact-line b{font-weight:600}
.contact-line span{color:var(--blue)}
.navbar{top:109px;left:0;width:1440px;height:51px;background:var(--blue);display:flex;align-items:center;padding-left:121px;gap:34px;color:var(--white);font-size:15px;font-weight:500;white-space:nowrap}
.navbar .register{position:absolute;right:112px;top:12px;height:28px;width:80px;background:var(--white);color:var(--ink);border-radius:4px;font-size:13px;display:flex;align-items:center;justify-content:center}
/* hero */
.hero-title{left:90px;top:285px;font-family:'Lora',serif;font-size:56px;line-height:62px;color:var(--ink);font-weight:400}
.hero-text{left:90px;top:432px;width:560px;font-size:19px;line-height:31px;color:var(--muted)}
.stats-label{left:90px;top:750px;font-family:'Lora',serif;font-size:20px;font-weight:500}
.stat{top:795px;font-family:'Lora',serif;font-size:30px;color:var(--blue)}
.stat small{display:block;font-family:'Inter',sans-serif;font-size:14px;color:var(--muted);margin-top:8px}
.badge{top:920px;background:#d9dde3}
.arch-outer{left:754px;top:270px;width:555px;height:636px;border:3px solid #a9d3f0;border-radius:278px 278px 22px 22px;padding:8px}
.arch-photo{width:100%;height:100%;border-radius:268px 268px 16px 16px;background:linear-gradient(180deg,#e7ebef 0%,#c9c4bc 55%,#8e7d6d 100%)}
.caption{left:715px;top:926px;width:648px;height:54px;background:#dcecf8;display:flex;align-items:center;justify-content:center;font-family:'Lora',serif;font-size:26px;font-weight:600;gap:8px;white-space:nowrap}
.caption i{font-size:22px;font-weight:400;color:var(--ink)}
.search{left:137px;top:1137px;width:1164px;height:40px;background:var(--white);border:1px solid var(--line);display:flex;align-items:center;font-size:13px;color:#a8aeb6;white-space:nowrap}
.search div{height:100%;display:flex;align-items:center;padding-left:18px;border-right:1px solid var(--line)}
.search .go{margin-left:auto;width:48px;height:40px;background:var(--blue);color:var(--white);justify-content:center;padding:0;border:none}
/* sections */
.band{left:0;width:1440px}
.h2{font-family:'Lora',serif;font-size:36px;font-weight:400;color:var(--ink);white-space:nowrap}
.sub{font-size:16px;color:var(--muted)}
.card{position:absolute;background:var(--white);border-radius:8px;box-shadow:0 4px 18px rgba(20,40,70,.08);overflow:hidden}
.card .img{height:219px;position:relative}
.tag{position:absolute;left:24px;top:22px;background:var(--red);color:var(--white);font-size:12px;font-weight:600;padding:4px 10px;border-radius:3px;letter-spacing:1px}
.card .title{font-family:'Lora',serif;font-size:20px;margin:22px 24px 4px;white-space:nowrap}
.card .loc{font-size:13px;color:var(--muted);margin:0 24px}
.card .meta{display:flex;gap:26px;font-size:12px;color:var(--muted);margin:20px 24px;white-space:nowrap}
.card .price{position:absolute;left:24px;bottom:30px;font-size:26px;color:var(--ink)}
.card .for{position:absolute;right:24px;bottom:34px;font-size:12px;letter-spacing:2px;font-weight:600}
.video{left:387px;top:2219px;width:660px;height:398px;background:var(--white);box-shadow:0 4px 20px rgba(20,40,70,.1)}
.video-screen{position:absolute;left:32px;top:30px;width:596px;height:306px;background:#efefef}
.photo-frame{position:absolute;background:var(--white);padding:12px;box-shadow:0 4px 20px rgba(20,40,70,.1)}
.photo-frame div{width:100%;height:100%}
.svc-icon{position:absolute;left:24px;top:145px;width:92px;height:92px;background:var(--blue);border-radius:12px;display:flex;align-items:center;justify-content:center}
.svc .title{margin-top:34px}
.svc .desc{font-size:14px;line-height:25px;color:var(--muted);margin:12px 24px 0}
.svc .more{position:absolute;left:24px;bottom:24px;font-size:14px;color:var(--blue);font-weight:500}
.review{position:absolute;top:5003px;width:384px;height:415px;background:var(--white);border-radius:8px;box-shadow:0 4px 18px rgba(20,40,70,.06);padding:40px 40px;overflow:hidden}
.stars{color:var(--star);font-size:26px;letter-spacing:2px;white-space:nowrap}
.review h4{font-size:16px;font-weight:600;margin-top:8px}
.review p{font-size:14px;line-height:25px;color:var(--muted);margin-top:34px}
.reviewer{position:absolute;left:40px;bottom:40px;display:flex;align-items:center;gap:14px;font-size:13px}
.reviewer .avatar{width:50px;height:50px;border-radius:50%;background:#b8c3cc}
.reviewer small{display:block;color:var(--muted)}
.form-box{left:371px;top:5746px;width:668px;height:703px;background:var(--white);padding:50px}
.form-box label{display:block;font-size:13px;font-weight:600;margin:22px 0 10px}
.field{height:40px;border:1px solid var(--line);border-radius:3px;font-size:13px;color:#a8aeb6;display:flex;align-items:center;padding-left:14px}
.partners{top:6710px;left:121px;width:1195px;display:flex;justify-content:space-around;align-items:center;height:56px;font-family:'Lora',serif;font-size:18px;letter-spacing:2px;color:#4a4f57}
.help{left:121px;top:6796px;width:1195px;height:274px;background:#f4f4f6;border-radius:14px}
.footer{left:0;top:6933px;width:1440px;height:614px;background:var(--footer);color:#d8d9db}
.footer .lbl{font-size:14px;color:#a6a8ad}
.footer .val{font-size:20px;color:var(--white)}
.social{display:flex;gap:36px}
.social span{width:22px;height:22px;border-radius:50%;background:#cfd1d4}
</style>
</head>
<body>
<div class="page">

  <!-- header -->
  <div class="abs topbar">
    <div class="abs brand" style="left:102px;top:30px"><span class="brand-mark"></span>Brightholt Residential</div>
    <svg class="abs" style="left:637px;top:40px" width="30" height="30" viewBox="0 0 24 24" fill="none" stroke="#3a3f47" stroke-width="1.6"><path d="M5 3h4l2 5-2.5 1.5a11 11 0 0 0 6 6L16 13l5 2v4a2 2 0 0 1-2 2A16 16 0 0 1 3 5a2 2 0 0 1 2-2z"/></svg>
    <div class="abs contact-line" style="left:687px;top:26px"><b>Phone:</b> <span>204-555-0142</span><br><b>Toll Free:</b> <span>1-800-555-0187</span></div>
    <svg class="abs" style="left:891px;top:40px" width="30" height="24" viewBox="0 0 24 18" fill="none" stroke="#3a3f47" stroke-width="1.6"><rect x="1" y="1" width="22" height="16" rx="2"/><path d="M1 2l11 8 11-8"/></svg>
    <div class="abs contact-line" style="left:934px;top:41px"><span>info@brightholtrm.com</span></div>
    <div class="btn btn-blue" style="left:1133px;top:31px;width:195px;height:43px;font-size:13px">Create maintenance ticket</div>
  </div>
  <nav class="abs navbar">
    <span>Home</span><span>Services ▾</span><span>Pricing ▾</span><span>Home watch</span><span>Leasing only</span><span>Rentals</span><span>FAQs</span><span>About us ▾</span>
    <span class="register">Register</span>
  </nav>

  <!-- hero -->
  <h1 class="abs hero-title">Where dream homes<br>become a reality.</h1>
  <p class="abs hero-text">Brightholt Residential Management has been serving the Winnipeg and surrounding areas since 1997. We offer world class management services to investors and tenants in the single family and multifamily rental market.</p>
  <div class="btn btn-blue" style="left:90px;top:598px;width:210px;height:40px">Find your next home</div>
  <div class="btn btn-ghost" style="left:316px;top:598px;width:190px;height:40px">Existing owner login</div>
  <div class="btn btn-ghost" style="left:90px;top:656px;width:210px;height:40px">Existing tenant login</div>
  <div class="btn btn-ghost" style="left:316px;top:656px;width:150px;height:40px">Our services</div>
  <div class="btn btn-ghost" style="left:482px;top:656px;width:160px;height:40px">Rent calculator</div>
  <div class="abs stats-label">Currently Under Management</div>
  <div class="abs" style="left:90px;top:785px;width:600px;height:1px;background:var(--line)"></div>
  <div class="abs stat" style="left:90px">447+<small>Properties</small></div>
  <div class="abs stat" style="left:305px">542+<small>Units</small></div>
  <div class="abs stat" style="left:520px">317+<small>Investors</small></div>
  <div class="abs badge" style="left:90px;top:938px;width:160px;height:48px;border-radius:4px"></div>
  <div class="abs badge" style="left:300px;top:922px;width:80px;height:80px;border-radius:50%;background:#cdd8e6"></div>
  <div class="abs badge" style="left:430px;top:922px;width:60px;height:80px;border-radius:30px;background:#d8c4b4"></div>
  <div class="abs arch-outer"><div class="arch-photo" role="img" aria-label="Bright living room with sofa, round coffee table, rug and ceiling fan"></div></div>
  <div class="abs caption"><span>No contract length!</span><i>Risk free, Stop any time.</i></div>
  <div class="abs search">
    <div style="width:510px">Enter Keyword...</div>
    <div style="width:110px">Status ⌄</div>
    <div style="width:110px">Type ⌄</div>
    <div style="width:125px">Bedrooms ⌄</div>
    <div style="width:135px">Pet friendly? ⌄</div>
    <div style="width:120px;color:var(--blue);border:none">⚙ Advanced</div>
    <div class="go">Go</div>
  </div>

  <!-- rentals -->
  <section class="abs band" style="top:1184px;height:820px;background:var(--grey-bg)">
    <h2 class="abs h2" style="left:121px;top:140px;font-size:34px">Winnipeg Rental Properties</h2>
    <p class="abs sub" style="left:121px;top:200px">Discover a wide range of properties for rent.</p>
    <div class="btn btn-ghost" style="left:980px;top:167px;width:215px;height:51px;font-size:14px">Browse all properties</div>
  </section>
  <div class="card" style="left:121px;top:1445px;width:387px;height:430px">
    <div class="img" role="img" aria-label="Modern white house with palm trees" style="background:linear-gradient(160deg,#6fa4d4,#cfd6da 55%,#5f7a55)"><span class="tag">★ FEATURED</span></div>
    <div class="title">18 Willow Bend Road</div><div class="loc">located in Maple Ridge</div>
    <div class="meta"><span>⌂ 3 beds</span><span>▭ 4 baths</span><span>⤢ 2450 sqft</span></div>
    <div class="price">$3095</div><div class="for">FOR RENT</div>
  </div>
  <div class="card" style="left:524px;top:1445px;width:391px;height:430px">
    <div class="img" role="img" aria-label="Two-storey family home with front lawn" style="background:linear-gradient(170deg,#5e92c6,#9fb0ba 50%,#4d6b3e)"><span class="tag">★ FEATURED</span></div>
    <div class="title">1420 Harlow Avenue West</div><div class="loc">located in Maple Ridge</div>
    <div class="meta"><span>⌂ 2 beds</span><span>▭ 1 baths</span><span>⤢ 2670 sqft</span></div>
    <div class="price">$1395</div><div class="for">FOR RENT</div>
  </div>
  <div class="card" style="left:930px;top:1445px;width:386px;height:430px">
    <div class="img" role="img" aria-label="Contemporary house lit at dusk" style="background:linear-gradient(170deg,#2e4a6e,#5a5f66 50%,#2f3b2c)"><span class="tag">★ FEATURED</span></div>
    <div class="title">305-210 Ashcombe Avenue</div><div class="loc">located in Maple Ridge</div>
    <div class="meta"><span>⌂ 1 beds</span><span>▭ 1 baths</span><span>⤢ 1680 sqft</span></div>
    <div class="price">$1995</div><div class="for">FOR RENT</div>
  </div>

  <!-- video + why -->
  <section class="abs band" style="top:2004px;height:1504px;background:var(--ice-bg)">
    <h2 class="abs h2" style="left:0;width:1440px;text-align:center;top:97px;font-size:34px">Is managing a property easy? Watch the video to find out!|</h2>
    <h2 class="abs h2" style="left:0;width:1440px;text-align:center;top:765px;font-size:34px">Why choose Brightholt as your property management company?</h2>
    <p class="abs sub" style="left:100px;width:1240px;text-align:center;top:830px;font-size:14px;line-height:24px">Brightholt Residential Management has been recognized and voted multiple times as The Best <span style="color:var(--blue)">Winnipeg Property Management</span> Company by Resident Laurel Prizes.<br>We are intently focused on serving both owners and tenants and are dedicated to a culture of superior customer service.<br>Whether you own one investment property or ten, the partnership process with Brightholt Residential Management is easy, efficient and rewarding.</p>
  </section>
  <div class="abs video">
    <div class="video-screen"><div style="position:absolute;left:290px;top:145px;width:18px;height:16px;background:#111;border-radius:3px"></div></div>
    <div class="abs" style="left:32px;top:360px;font-size:14px;color:#333;white-space:nowrap">⏮ ▶ ⏭ &nbsp;00:00</div>
    <div class="abs" style="left:160px;top:368px;width:468px;height:4px;background:#ddd;border-radius:2px"></div>
  </div>
  <div class="photo-frame" style="left:121px;top:2973px;width:563px;height:410px"><div role="img" aria-label="Couple reviewing lease documents with an agent" style="background:linear-gradient(135deg,#d9dee2,#8a9aa6 60%,#4d5660)"></div></div>
  <div class="photo-frame" style="left:730px;top:2973px;width:571px;height:410px"><div role="img" aria-label="Agent welcoming a couple into a new home" style="background:linear-gradient(135deg,#eef0f0,#b7b9b7 55%,#5d5a55)"></div></div>

  <!-- services -->
  <h2 class="abs h2" style="left:0;width:1440px;text-align:center;top:3640px">Our Services</h2>
  <p class="abs sub" style="left:0;width:1440px;text-align:center;top:3697px;font-size:14px">Brightholt Residential Management in Winnipeg offers some of the most premium services available for investors and tenants.</p>

  <div class="card svc" style="left:121px;top:3758px;width:387px;height:429px">
    <div class="img" role="img" aria-label="Large family house at twilight" style="height:215px;background:linear-gradient(180deg,#6c7fb0,#c3b6c7 60%,#8c8d8a)"></div>
    <div class="svc-icon"><svg width="50" height="50" viewBox="0 0 24 24" fill="none" stroke="#fff" stroke-width="1.6"><path d="M12 4l5 4v5h-10v-5z"/><path d="M3 14c3 0 5 2 9 6 4-4 6-6 9-6"/></svg></div>
    <div class="title">Property Management</div>
    <div class="desc">Using the latest technology and specially trained staff, we efficiently manage your property.</div>
    <div class="more">Learn more</div>
  </div>
  <div class="card svc" style="left:524px;top:3758px;width:391px;height:429px">
    <div class="img" role="img" aria-label="Open plan living room interior" style="height:215px;background:linear-gradient(180deg,#e6e3de,#c4beb5 60%,#8f867b)"></div>
    <div class="svc-icon"><svg width="50" height="50" viewBox="0 0 24 24" fill="none" stroke="#fff" stroke-width="1.6"><rect x="4" y="3" width="12" height="16" rx="1"/><path d="M7 7h6M7 10h6M7 13h3"/><circle cx="16" cy="16" r="3"/><path d="M18 18l3 3"/></svg></div>
    <div class="title">Leasing and Renewals</div>
    <div class="desc">We perform a comprehensive rental market evaluation to maximize your investment.</div>
    <div class="more">Learn more</div>
  </div>
  <div class="card svc" style="left:930px;top:3758px;width:386px;height:429px">
    <div class="img" role="img" aria-label="Empty room with large windows" style="height:215px;background:linear-gradient(180deg,#d7d9d8,#a9aca9 60%,#6f716f)"></div>
    <div class="svc-icon"><svg width="50" height="50" viewBox="0 0 24 24" fill="none" stroke="#fff" stroke-width="1.6"><circle cx="12" cy="7" r="3"/><path d="M3 15c3 0 5 2 9 5 4-3 6-5 9-5"/></svg></div>
    <div class="title">Property Maintenance</div>
    <div class="desc">You'll never have to worry about that midnight call or have to scramble to find a plumber.</div>
    <div class="more">Learn more</div>
  </div>
  <div class="card svc" style="left:121px;top:4219px;width:387px;height:429px">
    <div class="img" role="img" aria-label="Worker cutting metal with sparks" style="height:215px;background:linear-gradient(180deg,#5d5a55,#a88a62 60%,#3d3a36)"></div>
    <div class="svc-icon"><svg width="50" height="50" viewBox="0 0 24 24" fill="none" stroke="#fff" stroke-width="1.6"><circle cx="10" cy="5" r="2"/><path d="M10 8v6l-3 6M10 14l4 6M6 11h8"/></svg></div>
    <div class="title">Rehab and Construction</div>
    <div class="desc">We provide maintenance and repair services, and can also help you with larger construction projects.</div>
    <div class="more">Learn more</div>
  </div>
  <div class="card svc" style="left:524px;top:4219px;width:391px;height:429px">
    <div class="img" role="img" aria-label="Stacked cardboard moving boxes" style="height:215px;background:linear-gradient(180deg,#dad6d0,#c7a57c 60%,#8d6a48)"></div>
    <div class="svc-icon"><svg width="50" height="50" viewBox="0 0 24 24" fill="none" stroke="#fff" stroke-width="1.6"><path d="M12 11s-4-2.5-4-5a2 2 0 0 1 4-1 2 2 0 0 1 4 1c0 2.5-4 5-4 5z"/><path d="M3 15c3 0 5 2 9 5 4-3 6-5 9-5"/></svg></div>
    <div class="title">Free Stuff</div>
    <div class="desc">At Brightholt we want to help smaller landlords. We believe in "giving back" which is why we volunteer hundreds of hours per year.</div>
    <div class="more">Learn more</div>
  </div>

  <!-- reviews -->
  <section class="abs band" style="top:4770px;height:827px;background:var(--ice-bg)">
    <h2 class="abs h2" style="left:121px;top:130px;font-size:34px">See what our clients are saying in our latest Verified Reviews</h2>
    <div class="abs" style="left:1187px;top:136px;width:40px;height:40px;border-radius:50%;background:var(--white);text-align:center;line-height:40px;color:#aaa">‹</div>
    <div class="abs" style="left:1242px;top:136px;width:40px;height:40px;border-radius:50%;background:var(--white);text-align:center;line-height:40px;color:#aaa">›</div>
  </section>
  <div class="review" style="left:121px"><div class="stars">★★★★★</div><h4>Highly recommend!</h4><p>Thanks for helping us out, much appreciated.</p><div class="reviewer"><span class="avatar"></span><div>Owen Pratt<small>01/01/2023</small></div></div></div>
  <div class="review" style="left:528px"><div class="stars">★★★★★</div><h4>Above the expectations.</h4><p>Elliot has been incredibly helpful and his wealth of knowledge has been invaluable. He's been responsive (always getting back to me within the same day) and very easy to communicate with.</p><div class="reviewer"><span class="avatar"></span><div>Mira Castell<small>01/01/2023</small></div></div></div>
  <div class="review" style="left:934px"><div class="stars">★★★★★</div><h4>Easy and fast.</h4><p>I can't say enough good things about Property. They made the home buying process easy and stress-free. I highly recommend this company!</p><div class="reviewer"><span class="avatar"></span><div>Theo Marsh<small>01/01/2023</small></div></div></div>
  <div class="review" style="left:1344px"><div class="stars">★★★★★</div><h4>Highly</h4><p>"Worked absolutely professional responsive service</p><div class="reviewer"><span class="avatar"></span></div></div>

  <!-- contact -->
  <div class="abs band" role="img" aria-label="Softly lit living room with armchairs, rug and ceiling fan" style="top:5597px;height:1082px;background:linear-gradient(120deg,#6f86aa 0%,#9aa8c4 35%,#b3a7c0 70%,#9a7f9f 100%)"></div>
  <div class="abs form-box">
    <h3 class="serif" style="text-align:center;font-size:26px;font-weight:400;margin-bottom:24px">Contact Us</h3>
    <label>Name *</label>
    <div style="display:flex;gap:14px"><div class="field" style="flex:1">Enter you first name</div><div class="field" style="flex:1">Enter your last name</div></div>
    <label>Email Address *</label><div class="field">Enter your email address</div>
    <label>Phone number *</label><div class="field">Enter your Phone number</div>
    <label>What are you? *</label><div class="field" style="justify-content:space-between;padding-right:14px">Select<span>⌄</span></div>
    <label>Questions or Services interested in?</label><div class="field" style="height:100px"></div>
    <div class="btn btn-blue" style="position:relative;margin-top:28px;height:40px;font-size:14px">Submit</div>
  </div>
  <div class="abs partners"><span>STONEFIELD</span><span>Larkwood</span><span>NORTHVALE HOMES</span><span>CEDARLINE</span><span>ARDENT BUILDERS</span></div>

  <!-- footer -->
  <footer class="abs footer">
    <div class="abs brand" style="left:132px;top:236px;font-size:26px"><span class="brand-mark"></span>Brightholt Residential</div>
    <div class="abs" style="left:132px;top:314px"><div class="lbl">Phone support</div><div class="val" style="margin-top:8px">204-555-0142</div></div>
    <div class="abs" style="left:364px;top:314px"><div class="lbl">Email support</div><div class="val" style="margin-top:8px">info@brightholtrm.com</div></div>
    <div class="abs lbl" style="left:121px;top:446px">Follow us on social media</div>
    <div class="abs social" style="left:132px;top:485px"><span></span><span></span><span></span><span></span><span></span></div>
    <div class="abs" style="left:680px;top:212px;font-size:15px;color:var(--white)">Stay in touch with us</div>
    <div class="abs" style="left:680px;top:247px;width:500px;height:56px;background:#3a3a3d;border-radius:6px;font-size:14px;color:#8d8f94;padding:18px 16px">Your email address</div>
    <div class="abs btn" style="left:1180px;top:247px;width:125px;height:56px;background:#e9e9ea;color:var(--ink);font-size:14px">Subscribe</div>
    <div class="abs" style="left:680px;top:370px;font-size:15px;color:var(--white)">Sitemap</div>
    <div class="abs" style="left:680px;top:415px;font-size:14px;color:#a6a8ad;word-spacing:14px;white-space:nowrap">Home Services Rentals Pricing FAQs About&nbsp;us Contact&nbsp;us Contractors</div>
    <div class="abs" style="left:0;width:1440px;top:550px;text-align:center;font-size:12px;color:#a6a8ad">© 2023 Brightholt Residential Management. All right reserved.</div>
  </footer>
  <div class="abs help">
    <div class="abs" style="left:62px;top:100px;font-size:30px;font-weight:600;color:var(--ink);white-space:nowrap">Need help? Talk to our agents.</div>
    <div class="abs sub" style="left:62px;top:152px;font-size:15px">Get assistance from our friendly real estate agents.</div>
    <div class="btn btn-blue" style="left:713px;top:110px;width:190px;height:56px;font-size:14px">204-555-0142</div>
    <div class="btn btn-ghost" style="left:920px;top:110px;width:220px;height:56px;font-size:14px">info@brightholtrm.com</div>
  </div>

</div>
</body>
</html>
```